Start-up Cleaning Business Needs Professional Business Cards

Marisol's Butler Tidying, LLC, is a start-up business based in the Northern Virginia suburbs of Washington, DC. MBT provides cleaning and housekeeping services for homes and offices. We have three core values:

1. We are personal. We value knowing and being known by our customers and each other. If you want nameless, faceless service, you should choose another provider. We put "personal" at the front of the list, because it is most important to us; the design we choose will convey this value.

2. Like a hotel concierge, we are professional in attitude, posture, communication and processes.

3. Like a hotel concierge, we solve problems with a can-do attitude and never make excuses.

Our uniforms are khaki pants with pink polo shirts.

Our logo is attached. There are other symbols, not represented in our logo, that may convey our values well, such as a top hat and bow tie, magnifying glass, desk bell, etc.

Please include fields for an individual's name and title, office phone number, mobile phone number, email address and website address (www.marisolsbutlertidying-example.com).

Standard U.S. size: 2" x 3.5"
Updates

I should have mentioned that the purpose of all our advertising - business cards included - is to motivate potential customers to call or email to arrange a free in-home estimate.

```html
<!DOCTYPE html>
<html lang="en">
<head>
<meta charset="utf-8">
<title>Brightwell Home Care – Business Card</title>
<link href="https://fonts.googleapis.com/css2?family=Comfortaa:wght@400&family=Open+Sans:wght@400;600;700&display=swap" rel="stylesheet">
<style>
  :root {
    --stage: #e6e6e8;
    --card-pink-light: #fcecf3;
    --card-pink: #f3c4d9;
    --magenta: #d6257f;
    --magenta-deep: #b81a6b;
    --ink: #4a4a4a;
    --ink-soft: #8a8a8a;
    --ink-dark: #2b2b2b;
    --white: #ffffff;
  }
  * { box-sizing: border-box; margin: 0; padding: 0; }
  html, body {
    width: 1200px; height: 926px; overflow: hidden;
    background: var(--stage);
  }
  .canvas { position: relative; width: 1200px; height: 926px; }
  .card {
    position: absolute; left: 250px; width: 700px; height: 400px;
    overflow: hidden; border-radius: 3px;
    box-shadow: 0 6px 18px rgba(0,0,0,0.18);
  }

  /* front side */
  .card--front {
    top: 50px;
    background: radial-gradient(ellipse at 72% 55%, var(--white) 0%, var(--card-pink-light) 35%, var(--card-pink) 100%);
  }
  .brand {
    position: absolute; left: 44px; top: 36px;
    font-family: "Comfortaa", sans-serif; font-weight: 400; color: var(--ink);
  }
  .brand__name { font-size: 42px; line-height: 1; }
  .brand__tagline {
    margin-top: 6px; font-size: 13px; letter-spacing: 3px; color: var(--ink-soft);
  }
  .person { position: absolute; left: 44px; top: 140px; }
  .person__name {
    font-family: "Open Sans", sans-serif; font-weight: 400;
    font-size: 28px; color: var(--magenta); line-height: 1;
  }
  .person__name strong { font-weight: 700; }
  .person__title {
    margin-top: 4px;
    font-family: "Open Sans", sans-serif; font-size: 13px;
    letter-spacing: 1.5px; color: var(--ink-dark);
  }
  .contact {
    position: absolute; left: 44px; top: 226px; list-style: none;
    font-family: "Open Sans", sans-serif; font-size: 15px;
    line-height: 1.6; color: var(--ink-dark);
  }
  .contact__label { font-weight: 700; }
  .front-band {
    position: absolute; left: 0; right: 0; bottom: 0; height: 24px;
    background: var(--magenta);
  }
  .front-illustration {
    position: absolute; left: 430px; top: 40px; width: 240px; height: 330px;
    border-radius: 6px;
    background: linear-gradient(180deg, #f0b7d2 0%, #e98fbb 60%, #f5d3e3 100%);
    opacity: 0.85;
  }

  /* back side */
  .card--back {
    top: 476px;
    background: radial-gradient(ellipse at 50% 45%, var(--magenta) 0%, var(--magenta-deep) 100%);
  }
  .back-illustration {
    position: absolute; left: 280px; top: 40px; width: 160px; height: 200px;
    border-radius: 6px;
    background: linear-gradient(180deg, rgba(255,255,255,0.35) 0%, rgba(255,255,255,0.15) 100%);
  }
  .back-brand {
    position: absolute; left: 0; right: 0; top: 256px; text-align: center;
    font-family: "Comfortaa", sans-serif; font-weight: 400; color: var(--white);
  }
  .back-brand .brand__name { font-size: 40px; }
  .back-brand .brand__tagline { color: rgba(255,255,255,0.85); }
</style>
</head>
<body>
<main class="canvas">
  <section class="card card--front">
    <div class="brand">
      <p class="brand__name">Brightwell</p>
      <p class="brand__tagline">Home Care</p>
    </div>
    <div class="person">
      <p class="person__name">jane <strong>roe</strong></p>
      <p class="person__title">product manager</p>
    </div>
    <ul class="contact">
      <li><span class="contact__label">mobile:</span> 0912345678</li>
      <li><span class="contact__label">office phone:</span> 055-210-7788</li>
      <li><span class="contact__label">web:</span> www.brightwellhomecare-example.com</li>
      <li><span class="contact__label">email:</span> jane@brightwellhomecare-example.com</li>
    </ul>
    <div class="front-illustration" role="img" aria-label="Sketch-style illustration of a housekeeper in a pink uniform mopping the floor"></div>
    <div class="front-band"></div>
  </section>

  <section class="card card--back">
    <div class="back-illustration" role="img" aria-label="White line drawing of a housekeeper mopping the floor"></div>
    <div class="back-brand">
      <p class="brand__name">Brightwell</p>
      <p class="brand__tagline">Home Care</p>
    </div>
  </section>
</main>
</body>
</html>
```